Maple Lantern Kids - pictora Photospot

We are looking for an pictora type wal for our pediatric dental office. We are thinking it could be weaved into a whole bunch of what we do (i.e. potentially water marked or faded in the background on letterhead, as an pictroa type wall in the practice, as a banner or section of the home page on the website, on rack cards, etc.) I’m thinking it would utilize a nice fun cursive script for the wording "Maple Lantern Kids is the spot for...." and a bunch of different sized “spots” with meaningful words that speak to who we are. That list would include things like:

• Fun
• Smiles
• Laughter
• Caring
• Comfort
• Amazing
• Kids
• Toddlers
• Teens
• Friends
• Family
• Health
• Education
• Cheer
• Positivity
• Exceptional Care

From a color perspective….we could look at a couple of options. We could have one version that has it washed out and in the background (more subliminal). We could have one version that was consistent with the colors in our logo. And we could have one version that popped with more color by utilizing the colors in some of the artwork we use throughout the office (snowboard picture as an example)

Target Market(s)

Appeal to hip families with kids

Industry/Entity Type

Pediatric Dental

Font styles to use
Other font styles liked:
• something modern, hip, playful and fun

Colors
0054AA
0677BA
7BADD7
CADEEF
E8F1F8
0094D4
00A9DD
6FCCEA
C7EBF8
E9F6FB
00AB8E
00BBA5
67D7C9
C6EFE9
E9F9F6

Requirements
Must have
• Use of existing logo and a play on "spots" or polka dots with symbpolic wording. Must appeal to young parents and kiddos (including hip teens)
Should not have
• SHOULDNT BE OVER THE TOP KIDS.

```html
<!DOCTYPE html>
<html lang="en">
<head>
<meta charset="utf-8">
<title>Maple Lantern Kids – Spot Wall</title>
<link rel="stylesheet" href="https://fonts.googleapis.com/css2?family=Signika:wght@700&family=Varela+Round&family=Fjalla+One&family=Nunito:ital,wght@1,700&family=Righteous&display=swap">
<style>
  :root {
    --navy: #1b3a51;
    --navy-dot: #1e4459;
    --teal-dot: #4b7883;
    --pale-dot: #dcdcd0;
    --word: #9cc4d9;
    --title-outline: #b9d9ec;
    --wash-aqua: #d3f3f1;
    --wash-pink: #ecd6e6;
    --wash-mauve: #dccbd0;
    --paper: #ffffff;
    --bear-light: #cfe4f1;
    --bear-mid: #7fb0cf;
  }
  * { margin: 0; padding: 0; box-sizing: border-box; }
  html, body { width: 1200px; height: 900px; overflow: hidden; background: var(--paper); }
  .wall {
    position: relative;
    width: 1200px;
    height: 900px;
    overflow: hidden;
    background:
      radial-gradient(ellipse 420px 300px at 250px 650px, var(--wash-aqua), transparent 70%),
      radial-gradient(ellipse 380px 320px at 880px 500px, var(--wash-pink), transparent 70%),
      radial-gradient(ellipse 360px 260px at 1050px 180px, var(--wash-aqua), transparent 70%),
      radial-gradient(ellipse 320px 240px at 280px 180px, var(--wash-pink), transparent 70%),
      radial-gradient(ellipse 300px 240px at 80px 120px, var(--wash-mauve), transparent 70%),
      radial-gradient(ellipse 340px 240px at 620px 820px, var(--wash-aqua), transparent 70%),
      radial-gradient(ellipse 300px 220px at 950px 840px, var(--wash-mauve), transparent 70%),
      var(--paper);
  }
  .wall__texture { position: absolute; inset: 0; }
  .confetti { position: absolute; inset: 0; }
  .confetti .navy { fill: var(--navy-dot); }
  .confetti .teal { fill: var(--teal-dot); }
  .confetti .pale { fill: var(--pale-dot); opacity: .85; }

  .headline {
    position: absolute;
    top: 52px;
    left: 0;
    width: 1200px;
    text-align: center;
    font-family: "Signika", sans-serif;
    font-weight: 700;
    font-size: 62px;
    letter-spacing: -0.5px;
    color: var(--navy);
    text-shadow:
      3px 0 0 var(--title-outline), -3px 0 0 var(--title-outline),
      0 3px 0 var(--title-outline), 0 -3px 0 var(--title-outline),
      2px 2px 0 var(--title-outline), -2px 2px 0 var(--title-outline),
      2px -2px 0 var(--title-outline), -2px -2px 0 var(--title-outline);
  }

  .spot {
    position: absolute;
    left: calc(var(--x) - var(--r));
    top: calc(var(--y) - var(--r));
    width: calc(var(--r) * 2);
    height: calc(var(--r) * 2);
    border-radius: 50%;
    background: var(--navy);
    color: var(--word);
    display: flex;
    align-items: center;
    justify-content: center;
    text-align: center;
    line-height: 1.2;
  }
  .spot--round { font-family: "Varela Round", sans-serif; }
  .spot--condensed { font-family: "Fjalla One", sans-serif; }
  .spot--script { font-family: "Nunito", sans-serif; font-style: italic; font-weight: 700; letter-spacing: 1px; }
  .spot--display { font-family: "Righteous", sans-serif; letter-spacing: 1px; }

  .hub {
    position: absolute;
    left: 453px;
    top: 318px;
    width: 294px;
    height: 294px;
    border-radius: 50%;
    background: var(--navy);
  }
  .hub__emblem {
    position: absolute;
    left: 36px;
    top: 44px;
    width: 222px;
    height: 144px;
    border-radius: 48% 52% 40% 44% / 55% 50% 45% 45%;
    background: radial-gradient(ellipse at 45% 40%, var(--bear-light), var(--bear-mid));
  }
  .hub__place {
    position: absolute;
    left: 0;
    width: 100%;
    top: 196px;
    text-align: center;
    font-family: "Varela Round", sans-serif;
    font-size: 19px;
    font-weight: 700;
    letter-spacing: .5px;
    color: #f4f8fb;
  }
</style>
</head>
<body>
<main class="wall">
  <div class="wall__texture" role="img" aria-label="Soft paint-splash wash in aqua, pink and mauve"></div>

  <svg class="confetti" width="1200" height="900" viewBox="0 0 1200 900" aria-hidden="true">
    <g class="pale">
      <circle cx="333" cy="36" r="16"/><circle cx="667" cy="27" r="16"/><circle cx="525" cy="137" r="16"/>
      <circle cx="752" cy="137" r="16"/><circle cx="989" cy="144" r="16"/><circle cx="1148" cy="150" r="16"/>
      <circle cx="112" cy="320" r="22"/><circle cx="200" cy="367" r="22"/><circle cx="508" cy="284" r="22"/>
      <circle cx="815" cy="330" r="22"/><circle cx="991" cy="364" r="16"/><circle cx="1132" cy="299" r="16"/>
      <circle cx="824" cy="572" r="16"/><circle cx="1052" cy="575" r="18"/><circle cx="1141" cy="630" r="22"/>
      <circle cx="50" cy="617" r="16"/><circle cx="437" cy="612" r="16"/><circle cx="264" cy="825" r="16"/>
      <circle cx="500" cy="833" r="16"/><circle cx="728" cy="826" r="16"/><circle cx="963" cy="835" r="16"/>
    </g>
    <g class="teal">
      <circle cx="298" cy="156" r="17"/><circle cx="202" cy="292" r="22"/><circle cx="439" cy="301" r="22"/>
      <circle cx="706" cy="281" r="22"/><circle cx="883" cy="306" r="22"/><circle cx="1006" cy="299" r="22"/>
      <circle cx="111" cy="394" r="22"/><circle cx="364" cy="453" r="22"/><circle cx="791" cy="350" r="16"/>
      <circle cx="1105" cy="353" r="16"/><circle cx="796" cy="572" r="22"/><circle cx="1052" cy="595" r="22"/>
      <circle cx="1141" cy="551" r="22"/><circle cx="432" cy="629" r="22"/><circle cx="178" cy="629" r="16"/>
      <circle cx="584" cy="655" r="20"/><circle cx="815" cy="646" r="22"/><circle cx="75" cy="838" r="22"/>
      <circle cx="412" cy="836" r="16"/><circle cx="648" cy="862" r="16"/><circle cx="877" cy="856" r="16"/>
      <circle cx="1113" cy="863" r="16"/>
    </g>
    <g class="navy">
      <circle cx="79" cy="36" r="16"/><circle cx="508" cy="25" r="12"/><circle cx="843" cy="30" r="16"/>
      <circle cx="1137" cy="55" r="15"/><circle cx="85" cy="243" r="20"/><circle cx="323" cy="250" r="22"/>
      <circle cx="535" cy="258" r="22"/><circle cx="771" cy="212" r="18"/><circle cx="227" cy="467" r="22"/>
      <circle cx="790" cy="470" r="22"/><circle cx="990" cy="504" r="22"/><circle cx="466" cy="720" r="22"/>
      <circle cx="702" cy="727" r="22"/><circle cx="930" cy="720" r="22"/><circle cx="1128" cy="684" r="22"/>
    </g>
  </svg>

  <h1 class="headline">Maple Lantern Kids is the spot for....</h1>

  <div class="spot spot--round" style="--x:179px;--y:203px;--r:48px;font-size:34px">FUN</div>
  <div class="spot spot--condensed" style="--x:432px;--y:197px;--r:52px;font-size:27px">SMILES</div>
  <div class="spot spot--condensed" style="--x:643px;--y:218px;--r:43px;font-size:18px">LAUGHTER</div>
  <div class="spot spot--round" style="--x:891px;--y:207px;--r:52px;font-size:24px">CARING</div>
  <div class="spot spot--script" style="--x:1080px;--y:207px;--r:39px;font-size:13px">COMFORT</div>
  <div class="spot spot--condensed" style="--x:299px;--y:361px;--r:52px;font-size:19px">EXCEPTIONAL<br>CARE</div>
  <div class="spot spot--condensed" style="--x:899px;--y:413px;--r:46px;font-size:19px">TODDLERS</div>
  <div class="spot spot--round" style="--x:1103px;--y:450px;--r:52px;font-size:26px">TEENS</div>
  <div class="spot spot--round" style="--x:113px;--y:525px;--r:52px;font-size:17px">AMAZING</div>
  <div class="spot spot--round" style="--x:320px;--y:553px;--r:42px;font-size:28px">KIDS</div>
  <div class="spot spot--condensed" style="--x:924px;--y:600px;--r:52px;font-size:18px">POSITIVITY</div>
  <div class="spot spot--display" style="--x:181px;--y:751px;--r:52px;font-size:17px">FRIENDS</div>
  <div class="spot spot--round" style="--x:339px;--y:728px;--r:42px;font-size:18px">FAMILY</div>
  <div class="spot spot--round" style="--x:597px;--y:769px;--r:52px;font-size:23px">HEALTH</div>
  <div class="spot spot--condensed" style="--x:810px;--y:777px;--r:38px;font-size:14px">EDUCATION</div>
  <div class="spot spot--round" style="--x:1051px;--y:760px;--r:63px;font-size:32px">CHEER</div>

  <div class="hub">
    <div class="hub__emblem" role="img" aria-label="Walking bear with a small star, in soft watercolour blue"></div>
    <p class="hub__place">CEDAR HOLLOW, CA</p>
  </div>
</main>
</body>
</html>
```